Modular Cat Home Business Card

We need a business card for a modular and configurable cat playhouse, known as NookBox. NookBoxes can be integrated with human furniture. They come in cubes that are stackable, customizable and interchangeable.

Our name card should be in the shape of an isometric cube (not a normal business card size) with the NookBox logo inside the cube on one side of the namecard. If a home can be created inside the cube to show a homely environment, that could be an option. We are toying with the idea of having the cube side black and white and the flip side with our details, colorful. Our brand colours are pastel. They include pastel yellow, pink, purple, blue and orange. On the flip side, should be details including our name, position, email address, website, contact number.

The overall design should be clean, minimalistic, yet portray fun, happiness and quirky style. The product is design oriented so the name card should reflect likewise.

Target Market(s)

Cat Owners, Home owners, Mid 20s

Industry/Entity Type

Business

Contact Information for Business Card

Name, position, company name, phone number, email address, website. Name font should be bigger.

Colors
f8ba93
f9d9e8
ecdaeb
cee9f5
cfeae6
eaf2ce
fcf9cd
fce8d3
fbd4d5

Requirements
Must have
• The logo
• A variety of pastel colors
• A die cut in the form of a cube
Nice to have
• A home in the cube, to show furniture integration

```html
<!DOCTYPE html>
<html lang="en">
<head>
<meta charset="UTF-8">
<title>NookBox Cube Business Card</title>
<link href="https://fonts.googleapis.com/css2?family=Open+Sans:wght@400;700&display=swap" rel="stylesheet">
<style>
  :root {
    --backdrop: #2b2b2b;
    --pastel-yellow: #fcf9cd;
    --pastel-pink: #f9d9e8;
    --pastel-blue: #cee9f5;
    --pastel-orange: #f8ba93;
    --pastel-purple: #ecdaeb;
    --mono-top: #ffffff;
    --mono-left: #eeeeee;
    --mono-right: #1c1c1c;
    --ink: #111111;
    --ink-soft: #2a2a2a;
    --wordmark: #555a60;
  }
  * { margin: 0; padding: 0; box-sizing: border-box; }
  html, body { width: 1200px; height: 900px; overflow: hidden; }
  body {
    background: var(--backdrop);
    font-family: "Open Sans", sans-serif;
    position: relative;
  }
  .cube {
    position: absolute;
    top: 220px;
    width: 398px;
    height: 460px;
  }
  .cube-details { left: 121px; }
  .cube-brand { left: 681px; }
  .cube-shape {
    position: absolute;
    inset: 0;
    filter: drop-shadow(0 12px 24px rgba(0,0,0,0.5));
  }
  .face {
    position: absolute;
    width: 199px;
    height: 230px;
    transform-origin: 0 0;
    display: flex;
    flex-direction: column;
  }
  .face-left { left: 0; top: 115px; transform: skewY(30deg); align-items: center; justify-content: center; }
  .face-right { left: 199px; top: 230px; transform: skewY(-30deg); padding: 34px 14px 0 16px; }
  .brand-square {
    width: 112px;
    height: 112px;
    border: 3px solid var(--ink);
    display: flex;
    align-items: center;
    justify-content: center;
  }
  .brand-name { font-weight: 400; font-size: 22px; color: var(--ink); }
  .brand-tag {
    margin-top: 14px;
    font-size: 12px;
    letter-spacing: 8px;
    margin-right: -8px;
    color: var(--wordmark);
  }
  .person-name { font-weight: 700; font-size: 18px; color: var(--ink); line-height: 1.1; }
  .person-role {
    font-size: 10.5px;
    text-transform: uppercase;
    color: var(--ink-soft);
    margin-top: 4px;
    margin-bottom: 16px;
  }
  .contact-list { list-style: none; }
  .contact-list li {
    display: flex;
    align-items: center;
    gap: 8px;
    font-size: 10.5px;
    text-transform: uppercase;
    line-height: 1.6;
    color: var(--ink-soft);
    white-space: nowrap;
  }
  .contact-list svg { width: 9px; height: 9px; flex: none; }
</style>
</head>
<body>
  <section class="cube cube-details">
    <svg class="cube-shape" viewBox="0 0 398 460" aria-hidden="true">
      <polygon points="199,0 398,115 199,230 0,115" fill="var(--pastel-yellow)"/>
      <polygon points="0,115 199,230 199,460 0,345" fill="var(--pastel-pink)"/>
      <polygon points="199,230 398,115 398,345 199,460" fill="var(--pastel-blue)"/>
      <polyline points="0,115 199,230 398,115" fill="none" stroke="var(--pastel-orange)" stroke-width="2"/>
      <line x1="199" y1="230" x2="199" y2="460" stroke="var(--pastel-purple)" stroke-width="2"/>
    </svg>
    <div class="face face-left">
      <div class="brand-square"><span class="brand-name">NookBox</span></div>
      <div class="brand-tag">NOOKBOX</div>
    </div>
    <div class="face face-right">
      <h1 class="person-name">DANIEL HARPER</h1>
      <p class="person-role">Managing Director</p>
      <ul class="contact-list">
        <li>
          <svg viewBox="0 0 10 10"><path d="M2 0.5 L3.6 2.6 L2.8 3.6 Q4 6 6.4 7.2 L7.4 6.4 L9.5 8 L8.4 9.5 Q3.5 9 0.5 1.6 Z" fill="#111"/></svg>
          055-210 874 316
        </li>
        <li>
          <svg viewBox="0 0 10 10"><rect x="0.5" y="2" width="9" height="6.5" fill="#111"/><path d="M0.8 2.3 L5 5.6 L9.2 2.3" stroke="#cee9f5" stroke-width="0.9" fill="none"/></svg>
          hello@nookmail.com
        </li>
        <li>
          <svg viewBox="0 0 10 10"><circle cx="5" cy="5" r="4.5" fill="#111"/><path d="M0.5 5 H9.5 M5 0.5 Q2.4 5 5 9.5 M5 0.5 Q7.6 5 5 9.5" stroke="#cee9f5" stroke-width="0.7" fill="none"/></svg>
          www.nookboxhome.com
        </li>
      </ul>
    </div>
  </section>

  <section class="cube cube-brand">
    <svg class="cube-shape" viewBox="0 0 398 460" aria-hidden="true">
      <polygon points="199,0 398,115 199,230 0,115" fill="var(--mono-top)"/>
      <polygon points="0,115 199,230 199,460 0,345" fill="var(--mono-left)"/>
      <polygon points="199,230 398,115 398,345 199,460" fill="var(--mono-right)"/>
    </svg>
    <div class="face face-left">
      <div class="brand-square"><span class="brand-name">NookBox</span></div>
      <div class="brand-tag">NOOKBOX</div>
    </div>
  </section>
</body>
</html>
```